Christmas social media advert post

I am looking for an eye catching advert for use mainly on social media posts.
The following is the detail of the event.

Christmas special offer-
£10pp,– offer includes –
Half an hour Toboggan track,
Half an hour Slingshot paintballs (20 paintballs pp) and safe target archery (under cover and indoor ranges). Activities all the family from age 4 to grandparents can join in,
Also available – Add on indoor activities including Mini Curling, Bead Blitz, Safe axe throwing, Air juggler – from £3.50pp and age 6plus
Café open for hot food and drinks in the ‘Fireside Frost Lodge and the heated Christmas marquee.

A basic idea I put together for what I feel is the important information is -

Christmas Special offer -
Starts Saturday 20th December.
£10pp – offer includes –
Half an hour Slingshot paintballs (20 paintballs pp) and safe target archery (under cover and indoor ranges). Activities all the family from age 4 to grandparents can join in. Booking is essential - details on how below.
Also available Add on indoor activities - including Mini Curling, Bead Blitz, Safe axe throwing, Air juggler – from £3.50pp and age 6plus.
Ages start from 4 plus.
All activities are great for children and adults so perfect for families as well as friends, parties and get togethers.
Free huge car parks,
Booking is easy-
Just Message from messenger (on this post) or email
martin@hollowbrookleisurepark.co.uk for availability of your preferred date and time.

I would be happy to send the detailed information to enquiries if it meant a better looking advert / post.

Full details are in the picture uploads, feel free to use as much or as little of the information as you feel best.

```html
<!DOCTYPE html>
<html lang="en">
<head>
<meta charset="utf-8">
<title>Christmas Special Offer</title>
<link href="https://fonts.googleapis.com/css2?family=Great+Vibes&family=Montserrat:ital,wght@0,400;0,600;0,700;0,800;1,400&family=Oswald:wght@600&display=swap" rel="stylesheet">
<style>
  :root {
    --cream: #f6efe0;
    --cream-light: #fbf7ee;
    --gold-dark: #9a6a1c;
    --gold-mid: #c9962e;
    --gold-light: #f7d774;
    --ink: #111111;
    --white: #ffffff;
    --photo-green: #6f9a4a;
    --photo-blue: #4aa6d8;
    --photo-red: #b3273a;
    --photo-wood: #8a7158;
  }
  * { box-sizing: border-box; margin: 0; padding: 0; }
  html, body { width: 1200px; height: 1200px; overflow: hidden; }
  body { font-family: "Montserrat", Arial, sans-serif; color: var(--ink); }

  .poster {
    position: relative;
    width: 1200px;
    height: 1200px;
    overflow: hidden;
    background:
      radial-gradient(circle at 75% 20%, var(--cream-light) 0%, transparent 55%),
      radial-gradient(circle at 20% 70%, #fbf5e8 0%, transparent 50%),
      linear-gradient(160deg, #f3ead6 0%, var(--cream) 50%, #f1e6cf 100%);
  }

  .ornaments {
    position: absolute; left: 80px; top: 10px; width: 200px; height: 320px;
    background: radial-gradient(ellipse at 50% 40%, rgba(214,168,72,0.28) 0%, rgba(214,168,72,0.06) 70%, transparent 100%);
    border-radius: 40px;
  }

  .headline-script {
    position: absolute; left: 370px; top: 40px;
    font-family: "Great Vibes", cursive;
    font-size: 190px; line-height: 1;
    background: linear-gradient(90deg, var(--gold-mid) 0%, var(--gold-light) 35%, var(--gold-dark) 70%, var(--gold-mid) 100%);
    -webkit-background-clip: text; background-clip: text;
    color: transparent;
  }

  .offer-pill {
    position: absolute; left: 767px; top: 177px; width: 366px; height: 81px;
    border-radius: 41px;
    background: linear-gradient(90deg, var(--gold-dark) 0%, var(--gold-light) 40%, var(--gold-mid) 75%, var(--gold-dark) 100%);
    color: var(--white);
    font-weight: 800; font-size: 38px;
    display: flex; align-items: center; justify-content: center;
    letter-spacing: 0.5px;
  }

  .start-date {
    position: absolute; left: 555px; top: 258px; width: 530px;
    font-family: "Oswald", Impact, sans-serif; font-weight: 600;
    font-size: 58px; line-height: 1; text-align: center;
    transform: scaleY(1.08);
  }
  .start-date sup { font-size: 0.45em; vertical-align: 0.9em; }

  .includes-band {
    position: absolute; left: 0; top: 335px; width: 411px; height: 50px;
    border-radius: 0 25px 25px 0;
    background: linear-gradient(90deg, var(--gold-dark) 0%, var(--gold-light) 45%, var(--gold-mid) 80%, var(--gold-dark) 100%);
    font-size: 25px; padding-left: 88px; line-height: 50px;
  }

  .activity { position: absolute; top: 391px; width: 316px; }
  .activity--toboggan { left: 73px; }
  .activity--paintball { left: 443px; }
  .activity--archery { left: 813px; }
  .activity__card {
    height: 306px; background: var(--white);
    box-shadow: 0 10px 8px -8px rgba(0,0,0,0.35);
    padding-top: 35px; text-align: center;
  }
  .activity__photo { width: 209px; height: 201px; margin: 0 auto; }
  .photo--toboggan { background: linear-gradient(160deg, #b9a98f 0%, var(--photo-red) 55%, var(--photo-green) 100%); }
  .photo--paintball { background: radial-gradient(circle at 60% 60%, #e8b61a 0%, var(--photo-red) 25%, var(--photo-blue) 48%, #1b1b1b 80%); }
  .photo--archery { background: linear-gradient(120deg, #2b2b2b 0%, #4a4036 45%, var(--photo-wood) 100%); }
  .activity__title { font-weight: 700; font-size: 25px; margin-top: 20px; }
  .activity__note { font-size: 22px; line-height: 1.25; text-align: center; margin-top: 16px; }

  .booking-note { position: absolute; left: 78px; top: 800px; font-weight: 700; font-size: 25px; }
  .addons-intro { position: absolute; left: 78px; top: 836px; font-size: 18px; }
  .addons-list {
    position: absolute; left: 108px; top: 876px; list-style: none;
    font-weight: 700; font-size: 26px; line-height: 31px;
  }
  .addons-list li::before { content: "•"; font-size: 20px; margin-right: 14px; vertical-align: 2px; }
  .addons-price { position: absolute; left: 363px; top: 994px; font-style: italic; font-size: 17px; }

  .info-box {
    position: absolute; left: 691px; top: 845px; width: 497px; height: 228px;
    background: var(--ink); color: var(--white);
    border-radius: 25px 25px 0 0;
    padding: 20px 30px 0 29px;
    font-size: 16.5px; line-height: 20.5px;
  }
  .info-box p + p { margin-top: 20px; }
  .info-box__parking { font-weight: 800; font-size: 19px; text-align: right; margin-top: 10px; padding-right: 0; }

  .booking-band {
    position: absolute; left: 0; top: 1063px; width: 1200px; height: 137px;
    background: linear-gradient(90deg, var(--gold-dark) 0%, var(--gold-mid) 20%, var(--gold-light) 50%, var(--gold-mid) 80%, var(--gold-dark) 100%);
    text-align: center;
  }
  .booking-band__title {
    position: absolute; left: 89px; top: 20px;
    color: var(--white); font-weight: 800; font-size: 27px;
  }
  .booking-band__text { position: absolute; left: 0; top: 60px; width: 1200px; font-size: 19px; line-height: 22px; }
  .booking-band__text strong { font-weight: 600; }
</style>
</head>
<body>
<main class="poster">
  <div class="ornaments" role="img" aria-label="Gold line-art Christmas tree, bauble, snowflake and stars"></div>

  <h1 class="headline-script">Christmas</h1>
  <div class="offer-pill">SPECIAL OFFER</div>
  <p class="start-date">Starts: Saturday 20<sup>th</sup> December</p>

  <div class="includes-band">Our £10pp Includes:</div>

  <section class="activity activity--toboggan">
    <div class="activity__card">
      <div class="activity__photo photo--toboggan" role="img" aria-label="Children in helmets riding red sledges down a toboggan track"></div>
      <h2 class="activity__title">Toboggan Track</h2>
    </div>
    <p class="activity__note">Thrills: Half an hour of<br>sliding fun!</p>
  </section>

  <section class="activity activity--paintball">
    <div class="activity__card">
      <div class="activity__photo photo--paintball" role="img" aria-label="Paint-splattered target with a 10 bullseye"></div>
      <h2 class="activity__title">Slingshot Paintball</h2>
    </div>
    <p class="activity__note">Action: Half an hour<br>(20 paintballs pp)</p>
  </section>

  <section class="activity activity--archery">
    <div class="activity__card">
      <div class="activity__photo photo--archery" role="img" aria-label="Young archer drawing a bow at an indoor target range"></div>
      <h2 class="activity__title">Safe Target Archery:</h2>
    </div>
    <p class="activity__note">Indoor and undercover<br>ranges!</p>
  </section>

  <p class="booking-note">Booking is essential - details on how below.</p>
  <p class="addons-intro">Also available Add on indoor activities - including</p>
  <ul class="addons-list">
    <li>Mini Curling 🥌</li>
    <li>Bead Blitz Fun</li>
    <li>Safe Axe Throwing ⛏️</li>
    <li>Air Juggler 🎈</li>
  </ul>
  <p class="addons-price">– from £3.50pp and age 6plus.</p>

  <aside class="info-box">
    <p>Café open for hot food and drinks in the ‘Fireside Frost Lodge and the heated Christmas marquee.<br>Ages start from 4 plus.</p>
    <p>All activities are great for children and adults so perfect for families as well as friends, parties and get togethers.</p>
    <p class="info-box__parking">FREE HUGE CAR PARKS</p>
  </aside>

  <footer class="booking-band">
    <h2 class="booking-band__title">BOOKING IS EASY!</h2>
    <p class="booking-band__text">Just Message from messenger (on this post) or email <strong>martin@hollowbrookleisurepark.co.uk</strong><br>for availability of your preferred date and time.</p>
  </footer>
</main>
</body>
</html>
```